Bright, Fun and hard to forget home inspection business card.

We need a Business card design for a new Home Inspection company. We are building a brand that is bright, fun and easy to remember.

Target Market(s)

Anyone involed in buying and selling of homes.

Industry/Entity Type

Home Inspection

Contact Information for Business Card

Colin Marlowe Owner/Inspector

Wedsite- PorchAndRafterCheck.example
Phone: 253-555-0187
Email- ColinMarlowe@mailbox.example
WA Lic # 4806

Requirements
Must have
• BRQV LOGO somewhere on card.

```html
<!DOCTYPE html>
<html lang="en">
<head>
<meta charset="utf-8">
<title>Porch &amp; Rafter Check – Business Card</title>
<link rel="stylesheet" href="https://fonts.googleapis.com/css2?family=Open+Sans:wght@400;700&family=Cinzel:wght@400&display=swap">
<style>
  :root {
    --backdrop: #8b5e3c;
    --paper: #ffffff;
    --ink-black: #111111;
    --brand-orange: #ec5a24;
    --text-grey: #555555;
    --text-white: #ffffff;
  }
  * { margin: 0; padding: 0; box-sizing: border-box; }
  html, body {
    width: 1200px;
    height: 480px;
    overflow: hidden;
    background: var(--backdrop);
    font-family: "Open Sans", Arial, sans-serif;
  }
  .canvas {
    position: relative;
    width: 1200px;
    height: 480px;
  }
  .card {
    position: absolute;
    top: 90px;
    width: 475px;
    height: 272px;
    overflow: hidden;
  }
  .card--front { left: 84px; background: var(--paper); }
  .card--back { left: 592px; background: var(--ink-black); }

  .brand {
    position: absolute;
    display: flex;
    align-items: center;
    gap: 10px;
    font-family: "Open Sans", Arial, sans-serif;
    font-weight: 700;
    color: var(--brand-orange);
    line-height: 1.05;
    text-transform: uppercase;
  }
  .brand__dot {
    flex: none;
    border-radius: 50%;
    background: var(--brand-orange);
  }
  .card--front .brand { left: 108px; top: 52px; font-size: 26px; }
  .card--front .brand__dot { width: 34px; height: 34px; }
  .card--back .brand { left: 122px; top: 110px; font-size: 26px; }
  .card--back .brand__dot { width: 34px; height: 34px; }

  .contact {
    position: absolute;
    left: 82px;
    font-size: 11.5px;
    color: var(--text-grey);
    white-space: nowrap;
  }
  .contact__label { color: var(--brand-orange); }
  .contact--phone { top: 174px; }
  .contact--email { top: 174px; left: 190px; }
  .contact--web { top: 191px; }
  .contact--licence { top: 191px; left: 298px; color: var(--brand-orange); }

  .swoosh {
    position: absolute;
    left: 0;
    top: 0;
    width: 475px;
    height: 272px;
  }
  .swoosh__accent { fill: var(--brand-orange); }
  .swoosh__band { fill: var(--ink-black); }

  .holder {
    position: absolute;
    left: 162px;
    top: 242px;
    font-family: "Cinzel", Georgia, serif;
    color: var(--text-white);
    font-size: 17px;
    letter-spacing: 0.5px;
    white-space: nowrap;
  }
  .holder__title { font-size: 10.5px; }
</style>
</head>
<body>
<main class="canvas">

  <section class="card card--front" aria-label="Business card front">
    <div class="brand">
      <span class="brand__dot"></span>
      <span class="brand__name">Porch &amp; Rafter<br>Check</span>
    </div>

    <p class="contact contact--phone"><span class="contact__label">Tel:</span> 253-555-0187</p>
    <p class="contact contact--email"><span class="contact__label">Email:</span> ColinMarlowe@mailbox.example</p>
    <p class="contact contact--web">PorchAndRafterCheck.example</p>
    <p class="contact contact--licence">WA Lic # 4806</p>

    <svg class="swoosh" viewBox="0 0 475 272" aria-hidden="true">
      <path class="swoosh__accent" d="M0,238 Q110,220 262,216 Q120,232 0,262 Z"/>
      <path class="swoosh__band" d="M0,256 Q250,212 475,198 L475,272 L0,272 Z"/>
    </svg>

    <p class="holder">Colin Marlowe, <span class="holder__title">Owner/Inspector</span></p>
  </section>

  <section class="card card--back" aria-label="Business card back">
    <div class="brand">
      <span class="brand__dot"></span>
      <span class="brand__name">Porch &amp; Rafter<br>Check</span>
    </div>
  </section>

</main>
</body>
</html>
```